Maralby Information Posters for Student signage

Secondary school looking for some posters to display throughout the school with fresh designs using school colours and fitting with general feel of the school's graphic image. The final designs should be welcoming but clearly outline the required instructions. Sample designs that have been created by the school are attached with the relevant information that is required to appear on the signs. School would like a more dynamic design than the basic signs attached.
We are looking for:
- Large pop-up banner style size for the 2 posters called
"Ready for class" and "Morning Routine".
- Printable poster for the "Maralby Outdoor" sign.

Please incorporate a design feature of "the Maralby 1,2,3" into the posters and also use the Maralby Leaner values of Integrity, Compassion, Curiosity and Drive to help illustrate the content.

An option for design is to incorporate our school's first nations artwork into the design and i have also provided various extracts of design pieces that the school often uses in it's marketing materials.

Target Market(s)

Secondary School Students

Industry/Entity Type

Education

Colors
00AB8E
00BBA5
67D7C9
C6EFE9
E9F9F6
FFF300
FFF600
FEFA6F
FFFEC7
FFFEE8
FFC000
F8CF3A
FAE287
FDF2CF
FEFAEE

Requirements
Must have
• My project must have eyecatching graphics

```html
<!DOCTYPE html>
<html lang="en">
<head>
<meta charset="utf-8">
<title>Maralby Morning Routine</title>
<link rel="stylesheet" href="https://fonts.googleapis.com/css2?family=Poppins:wght@600;700;800&family=Crimson+Pro:ital,wght@1,700&family=Arimo&display=swap">
<style>
:root{
  --green:#224f33;
  --yellow:#ffe600;
  --yellow-soft:#fff36a;
  --white:#ffffff;
  --rule:#333333;
  --dots:#b9b9b9;
}
*{margin:0;padding:0;box-sizing:border-box}
html,body{width:1200px;height:849px;overflow:hidden;background:var(--white)}
.poster{position:relative;width:1200px;height:849px;overflow:hidden;background:var(--white);font-family:'Poppins',sans-serif;color:var(--green)}
.artwork{position:absolute;left:0;width:1200px}
.artwork--top{top:0;height:110px}
.artwork--bottom{top:0;height:849px}
.title{position:absolute;left:46px;top:98px;font-weight:800;font-size:108px;line-height:86px;letter-spacing:-3px;text-transform:uppercase}
.badge123{position:absolute;left:611px;top:109px;width:541px;height:89px;border:7px solid var(--yellow);border-radius:30px;background:var(--white);overflow:hidden}
.badge123__name{position:absolute;left:0;top:0;width:336px;height:100%;background:var(--yellow-soft);font-weight:700;font-size:52px;line-height:75px;padding-left:14px;letter-spacing:-1px}
.badge123__step{position:absolute;top:11px;width:52px;height:52px;border-radius:50%;background:var(--green);color:var(--white);font-weight:700;font-size:34px;line-height:52px;text-align:center}
.tagline{position:absolute;left:617px;top:208px;font-family:'Crimson Pro',serif;font-style:italic;font-weight:700;font-size:41px;white-space:nowrap}
.title-rule{position:absolute;left:529px;top:272px;width:621px;height:1px;background:var(--rule)}
.panel{position:absolute;top:328px;width:539px;height:344px;border:7px solid var(--yellow);border-radius:26px;background:var(--white)}
.panel--on-time{left:50px}
.panel--late{left:612px}
.panel__label{position:absolute;top:-29px;height:54px;border-radius:14px;background:var(--yellow);font-weight:800;font-size:33px;line-height:56px;text-align:center;letter-spacing:-1px;text-transform:uppercase}
.panel--on-time .panel__label{left:163px;width:195px}
.panel--late .panel__label{left:110px;width:306px}
.step{position:absolute;left:0;width:100%;height:70px}
.step__num{position:absolute;left:28px;top:0;width:68px;height:68px;border-radius:50%;background:var(--green);color:var(--white);font-weight:700;font-size:46px;line-height:70px;text-align:center}
.step__icon{position:absolute;left:115px;top:0;width:68px;height:68px;border-radius:50%;background:var(--yellow);display:flex;align-items:center;justify-content:center}
.step__icon svg{width:44px;height:44px}
.step__text{position:absolute;left:213px;top:50%;transform:translateY(-50%);font-weight:700;font-size:23.5px;line-height:25px}
.panel--late .step__text{left:213px}
.step--1{top:31px}
.step--2{top:140px}
.step--3{top:249px}
.divider{position:absolute;left:28px;width:466px;border-top:2px dotted var(--dots)}
.divider--a{top:120px}
.divider--b{top:223px}
.values{position:absolute;right:180px;top:756px;text-align:right}
.values__name{color:var(--white);font-weight:700;font-size:36px;line-height:42px}
.values__caption{color:var(--yellow);font-family:'Arimo',sans-serif;font-size:25px;line-height:30px}
.school-mark{position:absolute;left:1034px;top:712px;display:flex;align-items:center;gap:8px}
.school-mark__dot{width:18px;height:18px;border-radius:50%;background:var(--yellow)}
.school-mark__name{color:var(--yellow);font-weight:700;font-size:22px;line-height:26px}
</style>
</head>
<body>
<div class="poster">
  <svg class="artwork artwork--top" viewBox="0 0 1200 110" role="img" aria-label="Yellow First Nations dot artwork band">
    <path d="M0,0 H840 C700,40 560,100 330,100 C180,100 80,80 0,90 Z" fill="var(--yellow)"/>
  </svg>
  <svg class="artwork artwork--bottom" viewBox="0 0 1200 849" role="img" aria-label="Green First Nations dot artwork wave">
    <path d="M0,678 C180,690 280,792 520,782 C700,774 820,690 990,664 C1090,650 1150,652 1200,656 V849 H0 Z" fill="var(--green)"/>
  </svg>

  <h1 class="title">Morning<br>Routine</h1>

  <div class="badge123">
    <div class="badge123__name">The Maralby</div>
    <div class="badge123__step" style="left:350px">1</div>
    <div class="badge123__step" style="left:414px">2</div>
    <div class="badge123__step" style="left:475px">3</div>
  </div>
  <p class="tagline">Early is on time, on time is late!</p>
  <div class="title-rule"></div>

  <section class="panel panel--on-time">
    <h2 class="panel__label">On Time</h2>
    <div class="step step--1">
      <div class="step__num">1</div>
      <div class="step__icon"><svg viewBox="0 0 44 44"><circle cx="22" cy="22" r="18" fill="none" stroke="var(--green)" stroke-width="3"/><path d="M22 10 V22 L30 29" fill="none" stroke="var(--green)" stroke-width="3" stroke-linecap="round"/></svg></div>
      <p class="step__text">Arrive before<br>8:30 AM</p>
    </div>
    <div class="divider divider--a"></div>
    <div class="step step--2">
      <div class="step__num">2</div>
      <div class="step__icon"><svg viewBox="0 0 44 44"><g fill="var(--green)"><rect x="6" y="6" width="10" height="32"/><rect x="17" y="6" width="10" height="32"/><rect x="28" y="6" width="10" height="32"/></g><g stroke="var(--yellow)" stroke-width="1.5"><path d="M8 10h6M8 13h6M19 10h6M19 13h6M30 10h6M30 13h6"/></g></svg></div>
      <p class="step__text">Place Bag in<br>Locker</p>
    </div>
    <div class="divider divider--b"></div>
    <div class="step step--3">
      <div class="step__num">3</div>
      <div class="step__icon"><svg viewBox="0 0 44 44"><g fill="var(--green)"><circle cx="20" cy="8" r="4"/><path d="M14 14h12v10H14z"/><rect x="28" y="16" width="8" height="16"/><circle cx="12" cy="30" r="3"/><circle cx="20" cy="30" r="3"/><circle cx="28" cy="30" r="3"/><path d="M7 40c0-5 3-7 5-7s5 2 5 7zM15 40c0-5 3-7 5-7s5 2 5 7zM23 40c0-5 3-7 5-7s5 2 5 7z"/></g></svg></div>
      <p class="step__text">Arrive at Home Group /<br>House Assembly<br>before 8:40 AM</p>
    </div>
  </section>

  <section class="panel panel--late">
    <h2 class="panel__label">Running Late</h2>
    <div class="step step--1">
      <div class="step__num">1</div>
      <div class="step__icon"><svg viewBox="0 0 44 44"><g fill="var(--green)"><path d="M21 4h2v8h-2z"/><path d="M23 4h7l-2 2 2 2h-7z"/><path d="M12 20 22 12 32 20V38H12z"/><rect x="4" y="22" width="8" height="16"/><rect x="32" y="22" width="8" height="16"/></g><g fill="var(--yellow)"><rect x="19" y="30" width="6" height="8"/><circle cx="22" cy="21" r="2.5"/><rect x="6" y="26" width="2" height="3"/><rect x="36" y="26" width="2" height="3"/></g></svg></div>
      <p class="step__text">Sign in at<br>Student Services</p>
    </div>
    <div class="divider divider--a"></div>
    <div class="step step--2">
      <div class="step__num">2</div>
      <div class="step__icon"><svg viewBox="0 0 44 44"><g fill="var(--green)"><rect x="6" y="6" width="10" height="32"/><rect x="17" y="6" width="10" height="32"/><rect x="28" y="6" width="10" height="32"/></g><g stroke="var(--yellow)" stroke-width="1.5"><path d="M8 10h6M8 13h6M19 10h6M19 13h6M30 10h6M30 13h6"/></g></svg></div>
      <p class="step__text" style="top:70%">Place bag in Locker</p>
    </div>
    <div class="divider divider--b"></div>
    <div class="step step--3">
      <div class="step__num">3</div>
      <div class="step__icon"><svg viewBox="0 0 44 44"><g fill="var(--green)"><circle cx="20" cy="8" r="4"/><path d="M14 14h12v10H14z"/><rect x="28" y="16" width="8" height="16"/><circle cx="12" cy="30" r="3"/><circle cx="20" cy="30" r="3"/><circle cx="28" cy="30" r="3"/><path d="M7 40c0-5 3-7 5-7s5 2 5 7zM15 40c0-5 3-7 5-7s5 2 5 7zM23 40c0-5 3-7 5-7s5 2 5 7z"/></g></svg></div>
      <p class="step__text">Prompt arrival to<br>class expected</p>
    </div>
  </section>

  <div class="values">
    <p class="values__name">Integrity</p>
    <p class="values__caption">Maralby Learner Values</p>
  </div>
  <div class="school-mark">
    <span class="school-mark__dot"></span>
    <span class="school-mark__name">Maralby</span>
  </div>
</div>
</body>
</html>
```